Update, redesign www.quorvane.net. Put it on WordPress and migrate to new host site

My current website is www.quorvane.net. The text content is ok but the site look and feel is several years old and does not project a sense of innovation. I am looking for a more modern exciting look. It needs to be built on word press and I need help in in putting it with a new hosting service.

Target Market(s)

Established organizations

Industry/Entity Type

Business Consultant

Number of Pages Required

1 page

Font styles to use
Sans Serif

Colors

Designer to choose colors to be used in the design.

Requirements
Must have
• Simple. Easy to read and navigate
Nice to have
• Innovation, creativity especially the leadership of innovation. Reading the current text on www.quorvane.net should help you with ideas
Should not have
• Difficulty in me managing or adding content after it is built

```html
<!DOCTYPE html>
<html lang="en">
<head>
<meta charset="utf-8">
<title>quorvane — Innovation at Work</title>
<link rel="stylesheet" href="https://fonts.googleapis.com/css2?family=Poppins:wght@400;500;600;700&family=PT+Sans:wght@400;700&display=swap">
<style>
:root{
  --navy:#0b1150;
  --navy-deep:#050833;
  --red:#e30613;
  --ink:#1c1c1c;
  --text:#444;
  --muted:#888;
  --band:#f2f0f0;
  --footer:#2e2e30;
  --white:#fff;
}
*{box-sizing:border-box;margin:0;padding:0}
html,body{width:1200px;height:3175px;overflow:hidden}
body{font-family:"PT Sans",Arial,sans-serif;color:var(--text);background:var(--white)}
.page{position:relative;width:1200px;height:3175px;overflow:hidden}
.abs{position:absolute}
a{color:inherit;text-decoration:none}

/* hero */
.hero{left:0;top:0;width:1200px;height:720px;background:radial-gradient(ellipse at 60% 55%,#1a2590 0%,var(--navy) 45%,var(--navy-deep) 100%)}
.nav{right:140px;top:32px;display:flex;gap:28px;font-family:"Poppins",sans-serif;font-weight:600;font-size:12.5px;color:var(--white);letter-spacing:.2px}
.nav span.drop::after{content:" ▾";font-size:10px}
.brand-box{left:334px;top:91px;width:324px;height:59px;background:var(--white);border-radius:4px;display:flex;align-items:center;justify-content:center;gap:12px}
.brand-box .name{font-family:"Poppins",sans-serif;font-weight:700;font-size:30px;color:var(--red)}
.brand-box .tag{font-family:"PT Sans",sans-serif;font-size:16px;color:var(--ink)}
.hero-title{left:673px;top:230px;font-family:"Poppins",sans-serif;font-weight:700;font-size:42px;line-height:44px;color:var(--white)}
.hero-title em{font-style:normal;color:var(--red)}
.hero-copy{left:673px;top:330px;width:345px;font-size:16.5px;line-height:21px;color:#e6e8ff}
.btn{display:inline-flex;align-items:center;justify-content:center;background:var(--red);color:var(--white);font-family:"Poppins",sans-serif;font-weight:600;font-size:12px;box-shadow:0 3px 6px rgba(0,0,0,.25)}
.hero-btn{left:675px;top:421px;width:140px;height:40px;font-size:14px}
.arrow{font-size:54px;color:rgba(255,255,255,.7);font-family:"PT Sans",sans-serif;line-height:1}
.hero-wave{left:0;top:600px}

/* section titles */
.sec-title{left:0;width:1200px;text-align:center;font-family:"Poppins",sans-serif;font-weight:600;font-size:30px;color:var(--ink)}
.rule{left:577px;width:46px;height:2px;background:#aaa}

/* services */
.service{width:270px;text-align:center}
.service .ring{width:152px;height:152px;margin:0 auto;border-radius:50%;background:var(--white);border:6px solid #f3f3f3;box-shadow:0 0 0 1px #e2e2e2,0 4px 10px rgba(0,0,0,.06);display:flex;align-items:center;justify-content:center}
.service h3{margin-top:44px;font-family:"Poppins",sans-serif;font-weight:600;font-size:19px;color:var(--ink)}
.service p{margin:12px auto 0;width:225px;font-size:13.5px;line-height:17px;color:var(--text)}
.service .btn{position:absolute;left:86px;top:336px;width:97px;height:30px}

/* about */
.about{left:0;top:1234px;width:1200px;height:570px;background:var(--band)}
.about-photo{left:140px;top:1350px;width:421px;height:343px;background:linear-gradient(135deg,#cfd3d8 0%,#8a8f96 55%,#4c5058 100%)}
.about-curve{left:140px;top:1540px}
.dot{left:515px;top:1279px;width:54px;height:54px;border-radius:50%;background:#959595}
.about-title{left:618px;top:1344px;font-family:"Poppins",sans-serif;font-weight:600;font-size:30px;color:var(--ink)}
.about-title span{color:var(--red)}
.about-sub{left:618px;top:1386px;font-size:17px;color:var(--ink)}
.about-rule{left:618px;top:1416px;width:46px;height:2px;background:#aaa}
.about-copy{left:618px;top:1454px;width:446px;font-size:14.5px;line-height:19px;color:var(--text)}
.about-btn{left:620px;top:1627px;width:97px;height:30px}
.about-wave{left:0;top:1740px}

/* videos */
.video{left:205px;top:1919px;width:790px;height:436px;background:linear-gradient(160deg,#6d6a62 0%,#3b3934 55%,#1f1e1b 100%);box-shadow:0 8px 20px rgba(0,0,0,.25)}
.play{left:562px;top:2106px;width:76px;height:54px;border-radius:12px;background:var(--red);display:flex;align-items:center;justify-content:center}
.caption{left:252px;top:2300px;width:372px;height:72px;background:var(--white);padding:14px 22px;box-shadow:0 4px 10px rgba(0,0,0,.12)}
.caption h4{font-family:"Poppins",sans-serif;font-weight:600;font-size:18px;color:var(--ink)}
.caption p{font-size:12px;color:var(--text);margin-top:2px}
.arrow.dark{color:#b5b5b5}

/* clients */
.clients{left:0;top:2455px;width:1200px;height:400px;background:var(--band)}
.client{top:2607px;width:171px;height:91px;background:var(--white);display:flex;align-items:center;justify-content:center;font-family:"Poppins",sans-serif;font-weight:600;font-size:20px;color:#8c8c8c;box-shadow:0 2px 5px rgba(0,0,0,.06)}
.seal{width:54px;height:54px;border-radius:50%;background:#c4c4c4}

/* footer */
.footer-shape{left:0;top:2780px}
.foot-brand{left:144px;top:2894px;font-family:"Poppins",sans-serif;font-weight:600;font-size:46px;color:var(--white);letter-spacing:.5px}
.foot-col{top:2852px;font-size:12.5px;line-height:17.8px;color:#d8d8d8}
.foot-col h5{font-family:"Poppins",sans-serif;font-weight:600;font-size:12.5px;color:var(--white);margin-bottom:12px}
.social{display:flex;align-items:center;gap:12px;margin-bottom:14px}
.social i{display:block;width:26px;height:26px;border-radius:50%;background:#2a67c9}
.foot-line{left:451px;top:3068px;width:620px;height:1px;background:#4a4a4c}
.copyright{left:0;top:3114px;width:1200px;text-align:center;font-size:12px;color:#cfcfcf}
</style>
</head>
<body>
<div class="page">

  <!-- HERO -->
  <div class="abs hero" role="img" aria-label="Photograph of a businessman in a suit against a deep blue background with flowing wave lines"></div>
  <nav class="abs nav">
    <span class="drop">ABOUT</span><span class="drop">THOUGHT LEADERSHIP</span><span class="drop">SERVICES</span><span>VIDEOS</span><span>CONTACT</span>
  </nav>
  <div class="abs brand-box"><span class="name">quorvane</span><span class="tag">Innovation at Work</span></div>
  <h1 class="abs hero-title">INNOVATION AT<br>WORK<em>.</em></h1>
  <p class="abs hero-copy">With over 30 years of combines experience in innovating in thereal world we know what works and what doesn't.</p>
  <a class="abs btn hero-btn">READ MORE &nbsp;▸</a>
  <div class="abs arrow" style="left:48px;top:348px">‹</div>
  <div class="abs arrow" style="left:1118px;top:348px">›</div>
  <svg class="abs hero-wave" width="1200" height="130" viewBox="0 0 1200 130">
    <path d="M0 95 C300 50 520 55 700 62 C900 70 1050 72 1200 50 L1200 130 L0 130 Z" fill="#fff"/>
    <path d="M0 95 C300 50 520 55 700 62 C900 70 1050 72 1200 50" fill="none" stroke="#e30613" stroke-width="8"/>
  </svg>

  <!-- SERVICES -->
  <h2 class="abs sec-title" style="top:700px">Our Services</h2>
  <div class="abs rule" style="top:753px"></div>

  <div class="abs service" style="left:142px;top:802px">
    <div class="ring">
      <svg width="70" height="60" viewBox="0 0 70 60">
        <rect x="27" y="0" width="18" height="13" rx="2" fill="#e30613"/>
        <circle cx="14" cy="20" r="6" fill="#333"/><circle cx="56" cy="20" r="6" fill="#333"/>
        <path d="M6 30h16v16h-6v12h-4V36H6z" fill="#333"/><path d="M64 30H48v16h6v12h4V36h6z" fill="#333"/>
        <rect x="22" y="32" width="26" height="5" fill="#333"/><rect x="33" y="37" width="4" height="21" fill="#333"/>
      </svg>
    </div>
    <h3>Consulting</h3>
    <p>We coined the phrase "Innovation at Work" because it represents both our core philosophy about innovation and our applied approach to helping our clients implement it</p>
    <a class="btn">READ MORE</a>
  </div>

  <div class="abs service" style="left:466px;top:802px">
    <div class="ring">
      <svg width="60" height="60" viewBox="0 0 60 60">
        <circle cx="30" cy="18" r="13" fill="#333"/>
        <path d="M4 58c0-16 11-24 26-24s26 8 26 24z" fill="#333"/>
        <path d="M28 36h4l2 16-4 4-4-4z" fill="#e30613"/>
      </svg>
    </div>
    <h3>Executive Education</h3>
    <p>Although much has been written about innovation, its practical application is less well understood. For example, many organizations start their quest for innovation...</p>
    <a class="btn">READ MORE</a>
  </div>

  <div class="abs service" style="left:807px;top:802px">
    <div class="ring">
      <svg width="72" height="56" viewBox="0 0 72 56">
        <path d="M2 2h40v26H16l-8 8v-8H2z" fill="#333"/>
        <rect x="9" y="10" width="26" height="3" fill="#fff"/><rect x="9" y="17" width="18" height="3" fill="#fff"/>
        <path d="M30 22h40v24h-6v8l-8-8H30z" fill="#e30613"/>
        <rect x="37" y="30" width="26" height="3" fill="#fff"/><rect x="37" y="37" width="16" height="3" fill="#fff"/>
      </svg>
    </div>
    <h3>Speaking</h3>
    <p>quorvane's senior associates are all seasoned speakers and capable of giving talks on a range of topics including..</p>
    <a class="btn">READ MORE</a>
  </div>

  <!-- ABOUT -->
  <div class="abs about"></div>
  <div class="abs about-photo" role="img" aria-label="Two businessmen reviewing documents at a desk"></div>
  <svg class="abs about-curve" width="421" height="160" viewBox="0 0 421 160">
    <path d="M0 160 L0 120 C140 40 300 30 360 0 L421 0 L421 160 Z" fill="#f2f0f0"/>
    <path d="M0 120 C140 40 300 30 360 0 L421 0 L421 150 C380 100 280 70 0 160 Z" fill="#8e8e8e"/>
  </svg>
  <div class="abs dot"></div>
  <h2 class="abs about-title">About <span>quorvane</span></h2>
  <p class="abs about-sub">Order Innovation Leverage</p>
  <div class="abs about-rule"></div>
  <p class="abs about-copy">Innovation Leverage reveals 7 secret principles that can help any innovator overcome the roadblocks and blockheads that they will inevitably meet on the path to creativity. And these principles do not presuppose an innovation friendly culture. In fact, the profiles in this book will introduce you to innovators who have succeeded even when their organizations' culture was either not particularly friendly to new ideas or even downright hostile.</p>
  <a class="abs btn about-btn">READ MORE</a>
  <svg class="abs about-wave" width="1200" height="70" viewBox="0 0 1200 70">
    <path d="M0 60 C300 10 800 0 1200 40 L1200 70 L0 70 Z" fill="#fff"/>
    <path d="M0 60 C300 10 800 0 1200 40" fill="none" stroke="#dcdada" stroke-width="4"/>
  </svg>

  <!-- VIDEOS -->
  <h2 class="abs sec-title" style="top:1813px">Videos</h2>
  <div class="abs rule" style="top:1868px"></div>
  <div class="abs video" role="img" aria-label="Presenter speaking to an audience in a training room with projected slides"></div>
  <div class="abs play"><svg width="24" height="26" viewBox="0 0 24 26"><path d="M0 0l24 13L0 26z" fill="#fff"/></svg></div>
  <div class="abs caption">
    <h4>INTRO TO INNOVATION | 3:32</h4>
    <p>MARCUS HALLORAN - MONDAY, FEBRUARY 10, 2014</p>
  </div>
  <div class="abs arrow dark" style="left:122px;top:2108px">‹</div>
  <div class="abs arrow dark" style="left:1050px;top:2108px">›</div>

  <!-- CLIENTS -->
  <div class="abs clients"></div>
  <h2 class="abs sec-title" style="top:2504px">Our Clients</h2>
  <div class="abs rule" style="top:2560px"></div>
  <div class="abs arrow dark" style="left:92px;top:2625px;font-size:36px">‹</div>
  <div class="abs client" style="left:142px">ORVEX</div>
  <div class="abs client" style="left:328px">HALDEN</div>
  <div class="abs client" style="left:512px">BRISCO</div>
  <div class="abs client" style="left:698px"><div class="seal"></div></div>
  <div class="abs client" style="left:885px">TAVORA</div>
  <div class="abs arrow dark" style="left:1082px;top:2625px;font-size:36px">›</div>

  <!-- FOOTER -->
  <svg class="abs footer-shape" width="1200" height="395" viewBox="0 0 1200 395">
    <path d="M0 40 C400 0 800 -5 1200 45 L1200 395 L0 395 Z" fill="#2e2e30"/>
    <path d="M0 40 C400 0 800 -5 1200 45" fill="none" stroke="#e30613" stroke-width="8"/>
  </svg>
  <div class="abs foot-brand">quorvane</div>
  <div class="abs foot-col" style="left:451px">
    <h5>MENU</h5>
    <div>Home</div><div>About</div><div>Thought Leadership</div><div>Services</div><div>Videos</div><div>Contact</div>
  </div>
  <div class="abs foot-col" style="left:609px">
    <h5>ABOUT</h5>
    <div>Overview</div><div>Marcus Halloran</div><div>Philosophy</div><div>How We Work</div>
  </div>
  <div class="abs foot-col" style="left:764px">
    <h5>SERVICES</h5>
    <div>Consulting</div><div>Executive Education</div><div>Speaking</div>
  </div>
  <div class="abs foot-col" style="left:920px">
    <h5>CONNECT WITH US</h5>
    <div class="social"><i></i>Chatterly</div>
    <div class="social"><i></i>Tweetline</div>
    <div class="social"><i style="background:#0d2a5c"></i>Proflink</div>
  </div>
  <div class="abs foot-line"></div>
  <p class="abs copyright">Copyrights @ 2018 All Rights Reserved</p>
</div>
</body>
</html>
```